Brightwell Building Group Stationary Revamp

We need a full set of new stationary including business cards for our Public Sector Construction company based in the South East of England. We have a new logo (attached) that we want to launch and revamp all of our company literature. We are required to send a lot of correspondence to residents etc so a consistent theme is required across everything. Also attached is our existing templates.

Target Market(s)

We work for Council and government provided housing organisations and NOT private individuals. All of our clients represent government spent money, so we need to look professional and instantly recognisable brand.

Industry/Entity Type

Business

Colors

Designer to choose colors to be used in the design.

Requirements
Must have
• New fresh designs that utilise our new logo. And the letterhead needs to be able to be rolled out onto a word template so that all staff can type straight onto it rather than us having to have it printed first.
Nice to have
• I am looking forward to seeing your best efforts as designers.

```html
<!DOCTYPE html>
<html lang="en">
<head>
<meta charset="utf-8">
<title>Brightwell Building Group – Stationery</title>
<link href="https://fonts.googleapis.com/css2?family=Open+Sans:wght@400;600;700&display=swap" rel="stylesheet">
<style>
  :root {
    --backdrop: #e1e2e1;
    --paper: #ffffff;
    --ink: #111111;
    --black: #000000;
    --gold: #c0952c;
    --gold-line: #c9a650;
    --text-font: "Open Sans", Arial, sans-serif;
  }
  * { box-sizing: border-box; margin: 0; padding: 0; }
  html, body { width: 1200px; height: 1001px; overflow: hidden; }
  body { background: var(--backdrop); font-family: var(--text-font); color: var(--ink); position: relative; }

  .letterhead { position: absolute; left: 86px; top: 80px; width: 650px; height: 840px; background: var(--paper); }
  .brand { position: absolute; display: flex; align-items: center; gap: 6px; font-family: var(--text-font); font-weight: 600; color: var(--ink); white-space: nowrap; }
  .brand-dot { width: 10px; height: 10px; border-radius: 50%; background: var(--gold); flex: none; }
  .letterhead .brand { left: 24px; top: 64px; font-size: 14px; }
  .letterhead .rule { position: absolute; left: 24px; top: 721px; width: 600px; height: 1px; background: var(--gold-line); }
  .contact-list { list-style: none; position: absolute; }
  .contact-list li { display: flex; align-items: center; white-space: nowrap; }
  .contact-list svg { flex: none; fill: none; stroke: var(--gold); }
  .letterhead .contact-list { left: 24px; top: 740px; font-size: 13.5px; line-height: 16px; }
  .letterhead .contact-list svg { width: 11px; height: 11px; margin-right: 8px; stroke-width: 1.6; }
  .address { position: absolute; font-style: normal; text-align: right; }
  .letterhead .address { right: 26px; top: 772px; font-size: 13.5px; line-height: 16px; }
  .base-band { position: absolute; left: 0; bottom: 0; width: 100%; height: 12px; display: flex; }
  .base-band .gold { width: 324px; background: var(--gold); }
  .base-band .black { flex: 1; margin-left: 2px; background: var(--black); }

  .card { position: absolute; left: 803px; width: 314px; height: 181px; background: var(--paper); overflow: hidden; }
  .card-front { top: 318px; }
  .card-back { top: 546px; }
  .card-front .sweep { position: absolute; inset: 0; }
  .card-front .brand { left: 14px; top: 46px; font-size: 9px; gap: 4px; }
  .card-front .brand-dot { width: 7px; height: 7px; }
  .holder { position: absolute; right: 14px; top: 14px; text-align: right; color: var(--paper); }
  .holder-name { font-size: 14px; font-weight: 700; color: var(--gold); line-height: 16px; }
  .holder-role { font-size: 7.5px; line-height: 10px; }
  .card-front .address { position: static; margin-top: 5px; font-size: 7.5px; line-height: 10px; color: var(--paper); }
  .card-front .contact-list { left: 14px; top: 120px; font-size: 7.5px; line-height: 10px; }
  .card-front .contact-list svg { width: 6px; height: 6px; margin-right: 5px; stroke-width: 2; }

  .card-back .lockup { position: absolute; left: 0; right: 0; top: 72px; display: flex; flex-direction: column; align-items: center; gap: 8px; }
  .card-back .brand { position: static; font-size: 17px; gap: 8px; }
  .card-back .underline { width: 190px; height: 1px; background: var(--gold-line); }
</style>
</head>
<body>

<section class="letterhead" aria-label="Letterhead">
  <div class="brand"><span class="brand-dot"></span>Brightwell Building Group</div>
  <div class="rule"></div>
  <ul class="contact-list">
    <li><svg viewBox="0 0 12 12"><rect x="3" y="1" width="6" height="10" rx="1"/></svg>+44 (0)7712 480915</li>
    <li><svg viewBox="0 0 12 12"><path d="M1 5 Q6 1 11 5 L10 6 L8 5 L4 5 L2 6 Z"/><rect x="3" y="7" width="6" height="4"/></svg>+44 (0)20 8314 5520</li>
    <li><svg viewBox="0 0 12 12"><path d="M3 1 L5 3 L4 5 Q5 7 7 8 L9 7 L11 9 L9 11 Q3 10 1 3 Z"/></svg>+44 (0)20 8314 5527</li>
    <li><svg viewBox="0 0 12 12"><rect x="1" y="3" width="10" height="7"/><path d="M1 3 L6 7 L11 3"/></svg>martin.hale@brightwellgroup.co.uk</li>
    <li><svg viewBox="0 0 12 12"><circle cx="6" cy="6" r="5"/><ellipse cx="6" cy="6" rx="2" ry="5"/><path d="M1 6 H11"/></svg>www.brightwellgroup.co.uk</li>
  </ul>
  <address class="address">Harbour House,<br>12 Linden Road<br>Dartford, Kent, DA1 4QP</address>
  <div class="base-band"><span class="gold"></span><span class="black"></span></div>
</section>

<section class="card card-front" aria-label="Business card front">
  <svg class="sweep" viewBox="0 0 314 181" preserveAspectRatio="none">
    <path d="M57 0 C150 8 213 90 213 181 L314 181 L314 0 Z" fill="var(--black)"/>
    <path d="M60 1 C152 12 208 92 209 181" fill="none" stroke="var(--gold)" stroke-width="3"/>
  </svg>
  <div class="brand"><span class="brand-dot"></span>Brightwell Building Group</div>
  <div class="holder">
    <p class="holder-name">Martin Hale</p>
    <p class="holder-role">Managing Director</p>
    <address class="address">Harbour House,<br>12 Linden Road<br>Dartford, Kent, DA1 4QP</address>
  </div>
  <ul class="contact-list">
    <li><svg viewBox="0 0 12 12"><rect x="3" y="1" width="6" height="10" rx="1"/></svg>+44 (0)7712 480915</li>
    <li><svg viewBox="0 0 12 12"><path d="M1 5 Q6 1 11 5 L10 6 L8 5 L4 5 L2 6 Z"/><rect x="3" y="7" width="6" height="4"/></svg>+44 (0)20 8314 5520</li>
    <li><svg viewBox="0 0 12 12"><path d="M3 1 L5 3 L4 5 Q5 7 7 8 L9 7 L11 9 L9 11 Q3 10 1 3 Z"/></svg>+44 (0)20 8314 5527</li>
    <li><svg viewBox="0 0 12 12"><rect x="1" y="3" width="10" height="7"/><path d="M1 3 L6 7 L11 3"/></svg>martin.hale@brightwellgroup.co.uk</li>
    <li><svg viewBox="0 0 12 12"><circle cx="6" cy="6" r="5"/><ellipse cx="6" cy="6" rx="2" ry="5"/><path d="M1 6 H11"/></svg>www.brightwellgroup.co.uk</li>
  </ul>
</section>

<section class="card card-back" aria-label="Business card back">
  <div class="lockup">
    <div class="brand">Brightwell Building Group</div>
    <div class="underline"></div>
  </div>
</section>

</body>
</html>
```